epoxy and decorative concrete information flyer

I need an informational flyer/pamphlet showcasing all of the services we offer. Prime Resin offers a wide range of services. Epoxy flake systems for garages and commercial settings. stained concrete for patios and driveways. Stamped concrete with a large selection of designs. Cool decking for patios and around pools. <br/><br/>I'm looking for something proffessional and not too cluttered with info. <br/>Example: https://pics.sampleview.net/q3LmZtY8wRkP52HvX

Requirements
Must have
• Contact info phone 512-470-6128 primeresin.com info@primeresin.com
• A couple nice photos of what we do
• benefits of each service
• Epoxy is stain resistant, slip resistant, easy to clean and increases value of home.
• Stained and stamped concrete increases value of home and looks great.
• cool decking provides a much cooler surface for your feet in the summer months
Should not have
• color selections of epoxy
• I know my logo and website is red and black but I think that is too harsh of colors of a flyer. Please use more elegant and friendly colors.

```html
<!DOCTYPE html>
<html lang="en">
<head>
<meta charset="utf-8">
<title>Prime Resin Flyer</title>
<link rel="stylesheet" href="https://fonts.googleapis.com/css2?family=Montserrat:wght@400;600;700;800&family=Arimo:wght@400;700&family=Yellowtail&display=swap">
<style>
  :root {
    --page-bg: #000000;
    --paper: #f3f3f3;
    --paper-shade: #dedede;
    --ink: #1a1a1a;
    --red: #e52d2d;
    --gold: #d8b25a;
    --gold-dark: #a8812f;
    --gold-light: #f3dc9c;
    --white: #ffffff;
    --script-gold: #f2c230;
  }
  * { margin: 0; padding: 0; box-sizing: border-box; }
  html, body { width: 1200px; height: 1200px; overflow: hidden; }
  body { background: var(--page-bg); font-family: "Montserrat", sans-serif; color: var(--ink); position: relative; }

  .flyer {
    position: absolute; left: 183px; top: 36px; width: 830px; height: 1133px;
    background: linear-gradient(135deg, var(--white) 0%, var(--paper) 50%, var(--paper-shade) 100%);
    overflow: hidden;
  }

  .header { position: absolute; left: 0; top: 0; width: 100%; height: 211px; }
  .brand { position: absolute; left: 64px; top: 80px; display: flex; align-items: center; gap: 14px; }
  .brand-mark { width: 26px; height: 26px; background: var(--red); flex: none; }
  .brand-name { font-family: "Montserrat", sans-serif; font-weight: 800; font-size: 50px; color: var(--ink); letter-spacing: 1px; text-transform: uppercase; line-height: 46px; }

  .contact { position: absolute; left: 462px; top: 100px; }
  .contact-row { display: flex; align-items: center; gap: 12px; font-family: "Arimo", sans-serif; font-weight: 700; color: var(--ink); }
  .contact-phone { font-size: 36px; line-height: 40px; }
  .contact-email { font-size: 22px; margin-top: 4px; }
  .contact svg { flex: none; }

  .hero {
    position: absolute; left: 0; top: 211px; width: 100%; height: 393px;
    background: linear-gradient(180deg, #6b1a1a 0%, #3a2a2a 30%, #6f6f78 60%, #9a98a6 100%);
    border-top: 4px solid var(--gold);
    border-bottom: 5px solid var(--gold);
  }
  .hero-title { position: absolute; top: 53px; width: 100%; text-align: center; color: var(--white); font-size: 33px; line-height: 46px; font-weight: 400; letter-spacing: -0.5px; text-transform: uppercase; }
  .hero-title strong { font-weight: 700; }
  .hero-tagline { position: absolute; top: 140px; width: 100%; text-align: center; color: var(--white); font-weight: 700; font-size: 31px; }
  .hero-tagline .script { font-family: "Yellowtail", "Brush Script MT", cursive; font-weight: 400; font-size: 60px; color: var(--script-gold); margin-left: 8px; }

  .gallery { position: absolute; left: 0; top: 497px; width: 100%; height: 216px; }
  .gallery svg { position: absolute; top: 0; }

  .benefits { position: absolute; top: 722px; width: 100%; text-align: center; font-size: 15.5px; line-height: 26px; color: var(--ink); }

  .features { position: absolute; left: 61px; top: 817px; display: flex; gap: 15px; }
  .feature {
    width: 128px; height: 187px; background: var(--white);
    border: 3px solid var(--gold); box-shadow: 0 0 0 1px var(--gold-dark), 2px 3px 6px rgba(0,0,0,0.25);
    text-align: center; font-family: "Arimo", sans-serif; padding: 10px 6px 0;
  }
  .feature svg { display: block; margin: 0 auto 12px; }
  .feature-title { font-size: 12.5px; font-weight: 700; margin-bottom: 8px; }
  .feature-text { font-size: 10.5px; line-height: 12.5px; }
  .feature-note { color: var(--red); font-size: 9px; line-height: 11px; margin-top: 5px; letter-spacing: -0.3px; white-space: nowrap; }
  .feature-note strong { color: var(--ink); display: block; }

  .web-band {
    position: absolute; left: 0; top: 1026px; width: 100%; height: 82px;
    background: linear-gradient(180deg, var(--gold-light) 0%, var(--gold) 55%, var(--gold-dark) 100%);
    display: flex; align-items: center; justify-content: center;
    font-family: "Arimo", sans-serif; font-weight: 700; font-size: 44px; color: var(--ink);
  }
</style>
</head>
<body>
  <main class="flyer">
    <header class="header">
      <div class="brand">
        <span class="brand-mark"></span>
        <span class="brand-name">Prime<br>Resin</span>
      </div>
      <div class="contact">
        <div class="contact-row contact-phone">
          <svg width="26" height="30" viewBox="0 0 26 30"><rect width="26" height="30" rx="5" fill="#e52d2d"/><path d="M8 7c2 0 3 4 2 5l-1 1c1 2 2 4 4 5l1-1c1-1 5 0 5 2 0 2-2 4-4 3-5-2-9-6-10-11 0-2 1-4 3-4z" fill="#fff"/></svg>
          <span>512-470-6128</span>
        </div>
        <div class="contact-row contact-email">
          <svg width="26" height="18" viewBox="0 0 26 18"><rect width="26" height="18" rx="2" fill="#e52d2d"/><path d="M2 2l11 9 11-9" stroke="#fff" stroke-width="2" fill="none"/></svg>
          <span>info@primeresin.com</span>
        </div>
      </div>
    </header>

    <section class="hero" role="img" aria-label="Photo of a sports car wheel on a glossy flake epoxy garage floor">
      <h1 class="hero-title">Prime <strong>Resin</strong> Provides the <strong>Best</strong><br><strong>Flooring Solutions</strong> on the Market</h1>
      <p class="hero-tagline">Make Your Floor Look<span class="script">Great</span></p>
    </section>

    <section class="gallery">
      <svg style="left:91px" width="188" height="216" viewBox="0 0 188 216" role="img" aria-label="Photo of a gray flake epoxy floor">
        <defs><linearGradient id="g1" x1="0" y1="0" x2="0" y2="1"><stop offset="0" stop-color="#8a8a8e"/><stop offset="1" stop-color="#b9b8bd"/></linearGradient></defs>
        <polygon points="94,3 185,55 185,161 94,213 3,161 3,55" fill="url(#g1)" stroke="#d8b25a" stroke-width="5"/>
      </svg>
      <svg style="left:321px" width="188" height="216" viewBox="0 0 188 216" role="img" aria-label="Photo of a pool with cool decking around it">
        <defs><linearGradient id="g2" x1="0" y1="0" x2="1" y2="1"><stop offset="0" stop-color="#2b78c9"/><stop offset="1" stop-color="#5ec3e8"/></linearGradient></defs>
        <polygon points="94,3 185,55 185,161 94,213 3,161 3,55" fill="url(#g2)" stroke="#d8b25a" stroke-width="5"/>
      </svg>
      <svg style="left:551px" width="188" height="216" viewBox="0 0 188 216" role="img" aria-label="Photo of a finished flake epoxy garage floor">
        <defs><linearGradient id="g3" x1="0" y1="0" x2="0" y2="1"><stop offset="0" stop-color="#3a3a3c"/><stop offset="1" stop-color="#9d9ca0"/></linearGradient></defs>
        <polygon points="94,3 185,55 185,161 94,213 3,161 3,55" fill="url(#g3)" stroke="#d8b25a" stroke-width="5"/>
      </svg>
    </section>

    <p class="benefits">
      Epoxy is stain resistant, slip resistant, easy to clean and increases value of home.<br>
      Stained and stamped concrete increases value of home and looks great.<br>
      cool decking provides a much cooler surface for your feet in the summer months
    </p>

    <section class="features">
      <article class="feature">
        <svg width="60" height="46" viewBox="0 0 60 46"><g fill="#e52d2d" transform="translate(30 4) scale(1 0.6) rotate(45)"><rect x="0" y="0" width="13" height="13"/><rect x="16" y="0" width="13" height="13"/><rect x="32" y="0" width="13" height="13"/><rect x="0" y="16" width="13" height="13"/><rect x="16" y="16" width="13" height="13"/><rect x="32" y="16" width="13" height="13"/><rect x="0" y="32" width="13" height="13"/><rect x="16" y="32" width="13" height="13"/><rect x="32" y="32" width="13" height="13"/></g></svg>
        <h2 class="feature-title">APPEARANCE</h2>
        <p class="feature-text">Epoxy Floors look bright and clean. They're a smooth even surface is easy to maintain</p>
      </article>
      <article class="feature">
        <svg width="46" height="46" viewBox="0 0 46 46"><path d="M23 4c5 7 8 11 8 15a8 8 0 0 1-16 0c0-4 3-8 8-15z" fill="#e52d2d"/><path d="M4 30h10l8 4h10c3 0 3 4 0 4H20M4 42h24l14-9c2-2 0-5-3-3l-8 5" fill="none" stroke="#e52d2d" stroke-width="4" stroke-linejoin="round"/></svg>
        <h2 class="feature-title">RESISTANCE</h2>
        <p class="feature-text">Our epoxy is highly resistance to just about everything including: oil,gas, bleach, cleansers, tires marks and more</p>
      </article>
      <article class="feature">
        <svg width="46" height="46" viewBox="0 0 46 46"><circle cx="23" cy="19" r="16" fill="#e52d2d"/><path d="M14 33l-4 11 6-3 4 5 3-9M32 33l4 11-6-3-4 5-3-9" fill="#e52d2d"/><text x="23" y="26" text-anchor="middle" font-family="Arimo, sans-serif" font-weight="700" font-size="20" fill="#fff">$</text></svg>
        <h2 class="feature-title">AFFORDABILITY</h2>
        <p class="feature-text">The price can't be beat by other professional installers.</p>
        <p class="feature-note"><strong>This Includes:</strong>-Base color coat with Flakes<br>-Clear coat with Anti Skid</p>
      </article>
      <article class="feature">
        <svg width="46" height="46" viewBox="0 0 46 46"><path d="M23 2l18 6v14c0 11-8 19-18 22C13 41 5 33 5 22V8z" fill="#e52d2d"/><path d="M15 16h14v6H15zM21 22h3v14h-3z" fill="#fff"/></svg>
        <h2 class="feature-title">DURABILITY</h2>
        <p class="feature-text">We use 100% solids epoxy which resists chipping, peeling, fading and stains. Then we top it off with a commercial grade clear coat.</p>
      </article>
      <article class="feature">
        <svg width="54" height="46" viewBox="0 0 54 46"><g fill="#e52d2d" stroke="#fff" stroke-width="1.5"><rect x="22" y="4" width="11" height="36" rx="1" transform="rotate(-30 27 40)"/><rect x="22" y="4" width="11" height="36" rx="1" transform="rotate(-12 27 40)"/><rect x="22" y="4" width="11" height="36" rx="1" transform="rotate(8 27 40)"/><rect x="22" y="4" width="11" height="36" rx="1" transform="rotate(28 27 40)"/></g><circle cx="27" cy="37" r="2" fill="#fff"/></svg>
        <h2 class="feature-title">VARIETY</h2>
        <p class="feature-text">We offer a large selection of colors to brighten up your garage.</p>
      </article>
    </section>

    <footer class="web-band">www.primeresin.com</footer>
  </main>
</body>
</html>
```